General contractor/GM consaltant business card

I need a card for my contracting company in North Dakota, we build industrial buildings for the oil feild and oil feild related companies offices, shops, airplain hangars, airports ext. We have a familly atmosphere on the job and are very relational and personal.
Industry/Entity Type
Industrial
Contact Information for Business Card
Kestrelmoor Builders LLC.
Dwight T.Halvorsun
4736 Quillfern dr. Colorado Springs, CO. 80927
Cell# 406-555-8142
dwight@kestrelmoorbuilders.com

```html
<!DOCTYPE html>
<html lang="en">
<head>
<meta charset="utf-8">
<title>Kestrelmoor Builders LLC. – Business Card</title>
<link rel="stylesheet" href="https://fonts.googleapis.com/css2?family=Cinzel:wght@700&family=Source+Sans+3:wght@400&display=swap">
<style>
  :root {
    --navy: #1f2266;
    --gold: #f7c51e;
    --sky: #5bb8e0;
    --sky-pale: #aadde3;
    --white: #ffffff;
    --backdrop-center: #f4f4f5;
    --backdrop-edge: #c4c5c8;
  }
  * { margin: 0; padding: 0; box-sizing: border-box; }
  html, body { width: 1200px; height: 1200px; overflow: hidden; }
  body {
    position: relative;
    background: radial-gradient(circle at 50% 50%, var(--backdrop-center) 0%, var(--backdrop-edge) 75%);
    font-family: "Source Sans 3", Arial, sans-serif;
  }
  .card { position: absolute; left: 228px; width: 742px; overflow: hidden; }

  /* Front */
  .card-front { top: 172px; height: 421px; background: var(--navy); }
  .front-header { position: absolute; left: 0; top: 0; width: 742px; height: 214px; background: var(--white); }
  .gold-band { position: absolute; left: 0; top: 196px; width: 450px; height: 18px; background: var(--gold); }
  .header-art {
    position: absolute; left: 450px; top: 26px; width: 292px; height: 188px;
    background: linear-gradient(90deg, var(--sky-pale) 0%, var(--sky) 100%);
  }
  .brand { position: absolute; display: flex; align-items: center; }
  .brand-dot { border-radius: 50%; background: var(--gold); flex: none; }
  .brand-name {
    font-family: "Cinzel", Georgia, serif; font-weight: 700; line-height: 1.1; letter-spacing: 1px;
  }
  .brand-front { left: 50px; top: 58px; gap: 38px; }
  .brand-front .brand-dot { width: 70px; height: 70px; }
  .brand-front .brand-name { color: var(--navy); font-size: 34px; }
  .holder-name {
    position: absolute; left: 34px; top: 292px;
    font-family: "Cinzel", Georgia, serif; font-weight: 700;
    font-size: 24px; letter-spacing: 3px; color: var(--white);
  }
  .contact {
    position: absolute; right: 24px; top: 241px;
    list-style: none; color: var(--white); font-size: 20px; line-height: 28px; text-align: right;
  }
  .contact li { display: flex; justify-content: flex-end; align-items: flex-start; gap: 12px; }
  .contact .phone { margin-top: 10px; }
  .contact .email { margin-top: 1px; }
  .contact .icon {
    width: 20px; height: 20px; border-radius: 50%; background: var(--gold);
    flex: none; margin-top: 4px; display: flex; align-items: center; justify-content: center;
  }
  .contact .icon svg { width: 12px; height: 12px; }

  /* Back */
  .card-back { top: 600px; height: 424px; background: var(--navy); }
  .back-art {
    position: absolute; left: 0; top: 20px; width: 742px; height: 360px;
    background: linear-gradient(180deg, rgba(255,255,255,0) 0%, rgba(255,255,255,0.04) 60%, rgba(255,255,255,0) 100%);
  }
  .brand-back { left: 120px; top: 154px; gap: 60px; }
  .brand-back .brand-dot { width: 90px; height: 90px; }
  .brand-back .brand-name { color: var(--white); font-size: 48px; }
</style>
</head>
<body>

<section class="card card-front">
  <div class="front-header">
    <div class="gold-band"></div>
    <div class="header-art" role="img" aria-label="Building towers illustration"></div>
    <div class="brand brand-front">
      <span class="brand-dot"></span>
      <span class="brand-name">Kestrelmoor<br>Builders LLC.</span>
    </div>
  </div>

  <h1 class="holder-name">DWIGHT T.HALVORSUN</h1>

  <ul class="contact">
    <li class="address"><span>4736 Quillfern<br>dr. Colorado Springs,<br>CO. 80927</span>
      <span class="icon"><svg viewBox="0 0 12 12"><path d="M1 6 L6 1.5 L11 6 L9.5 6 L9.5 10.5 L2.5 10.5 L2.5 6 Z" fill="#1f2266"/></svg></span></li>
    <li class="phone"><span>406 - 555 - 8142</span>
      <span class="icon"><svg viewBox="0 0 12 12"><rect x="3.5" y="1" width="5" height="10" rx="1" fill="#1f2266"/><rect x="4.5" y="2.3" width="3" height="5.5" fill="#f7c51e"/></svg></span></li>
    <li class="email"><span>dwight@kestrelmoorbuilders.com</span>
      <span class="icon"><svg viewBox="0 0 12 12"><rect x="1.5" y="3" width="9" height="6.5" fill="#1f2266"/><path d="M1.5 3 L6 7 L10.5 3" stroke="#f7c51e" stroke-width="0.9" fill="none"/></svg></span></li>
  </ul>
</section>

<section class="card card-back">
  <div class="back-art" role="img" aria-label="Faint building perspective decoration"></div>
  <div class="brand brand-back">
    <span class="brand-dot"></span>
    <span class="brand-name">Kestrelmoor<br>Builders LLC.</span>
  </div>
</section>

</body>
</html>
```